I need a new business card design for my pharmacy.

I need a business card design. I will include my logo.
The card needs to be readable. I prefer to have my logo on one side along with my website, the other side includes the other information. Please use combination of black, neon green, white, and silver. This needs to catch the eye but yet be clearly visible and legible. Thanks

Industry/Entity Type

Pharmacy

Contact Information for Business Card

It needs to have the following information listed:
Mel's Apothecary Owner/Pharm D.
7134 North Brook Lane
Cedar Hollow, ND 58321
Phone 555-318-6207
Fax 555-318-6209
email: mel@melsapothecary-example.com
www.melsapothecary-example.com
Store hours Monday-Friday 9 am- 6 pm
Saturday 9 am- 1 pm
Sunday Closed
Please utilize the colors black, white, and neon green, maybe silver.

Requirements
Must have
• It needs to be easily readable!
Nice to have
• It should catch the eye.
Should not have
• Do not use any other colors except listed: black, neon green, white, & silver.

```html
<!DOCTYPE html>
<html lang="en">
<head>
<meta charset="utf-8">
<title>Mel's Apothecary — Business Card</title>
<link rel="stylesheet" href="https://fonts.googleapis.com/css2?family=Alegreya+Sans:wght@400;500&family=Open+Sans:wght@600&display=swap">
<style>
  :root {
    --backdrop: #efeeee;
    --paper: #ffffff;
    --ink: #1f1f1f;
    --lime: #a6ce39;
    --silver: #e4e5e7;
    --gap-line: #e9eef0;
  }
  * { box-sizing: border-box; margin: 0; padding: 0; }
  html, body {
    width: 1200px; height: 1200px; overflow: hidden;
    background: var(--backdrop);
  }
  .canvas { position: relative; width: 1200px; height: 1200px; }
  .card {
    position: absolute;
    width: 780px; height: 446px;
    background: var(--paper);
    box-shadow: 4px 6px 8px rgba(0,0,0,0.35);
    overflow: hidden;
    font-family: "Alegreya Sans", "Candara", sans-serif;
    font-variant-numeric: lining-nums;
    color: var(--ink);
  }
  .card--front { left: 104px; top: 84px; }
  .card--back  { left: 301px; top: 646px; }

  .rule { position: absolute; left: 0; right: 0; top: 312px; height: 6px; background: var(--lime); }
  .rule-gap { position: absolute; left: 0; right: 0; top: 318px; height: 10px; background: var(--gap-line); }
  .band { position: absolute; left: 0; right: 0; top: 328px; bottom: 0; background: var(--lime); }

  /* Front */
  .brand-dot {
    position: absolute; left: 42px; top: 112px;
    width: 84px; height: 84px; border-radius: 50%;
    background: var(--lime);
  }
  .brand-divider {
    position: absolute; left: 225px; top: 84px;
    width: 3px; height: 140px; background: var(--ink);
  }
  .brand-name {
    position: absolute; left: 264px; top: 112px;
    font-family: "Open Sans", sans-serif; font-weight: 600;
    font-size: 61px; letter-spacing: -1.8px; line-height: 1;
    color: var(--ink); white-space: nowrap;
  }
  .website {
    position: absolute; left: 0; right: 0; top: 394px;
    text-align: center; font-size: 26px; font-weight: 500;
    letter-spacing: 0.3px;
  }

  /* Back */
  .faint-mark {
    position: absolute; left: 40px; top: 50px;
    width: 240px; height: 240px; border-radius: 50%;
    background: var(--silver); opacity: 0.6;
  }
  .title-block {
    position: absolute; right: 32px; top: 42px; text-align: right;
  }
  .owner-title { font-size: 40px; font-weight: 500; line-height: 1; white-space: nowrap; }
  .credential {
    font-family: "Open Sans", sans-serif; font-weight: 600;
    font-size: 20px; color: var(--lime); margin-top: 0;
  }
  .contacts { position: absolute; left: 340px; top: 140px; }
  .contact-row { display: flex; height: 45px; align-items: center; font-size: 26px; }
  .contact-label { width: 70px; color: var(--lime); }
  .contact-sep { width: 15px; color: var(--lime); }
  .contact-value { white-space: nowrap; font-weight: 500; }
  .contact-value--email { font-size: 23px; }

  .address, .hours {
    position: absolute; top: 331px;
    font-size: 25px; font-weight: 500; line-height: 37px;
    white-space: nowrap;
  }
  .address { left: 25px; }
  .hours { left: 474px; }
</style>
</head>
<body>
<div class="canvas">

  <section class="card card--front">
    <div class="brand-dot"></div>
    <div class="brand-divider"></div>
    <div class="brand-name">Mel's Apothecary</div>
    <div class="rule"></div>
    <div class="rule-gap"></div>
    <div class="band"></div>
    <div class="website">www.melsapothecary-example.com</div>
  </section>

  <section class="card card--back">
    <div class="faint-mark"></div>
    <div class="title-block">
      <div class="owner-title">Mel's Apothecary Owner</div>
      <div class="credential">Pharm D.</div>
    </div>
    <div class="contacts">
      <div class="contact-row"><span class="contact-label">Phone</span><span class="contact-sep">:</span><span class="contact-value">555-318-6207</span></div>
      <div class="contact-row"><span class="contact-label">Fax</span><span class="contact-sep">:</span><span class="contact-value">555-318-6209</span></div>
      <div class="contact-row"><span class="contact-label">Email</span><span class="contact-sep">:</span><span class="contact-value contact-value--email">mel@melsapothecary-example.com</span></div>
    </div>
    <div class="rule"></div>
    <div class="rule-gap"></div>
    <div class="band"></div>
    <div class="address">
      7134 North Brook Lane<br>
      Cedar Hollow,<br>
      ND 58321
    </div>
    <div class="hours">
      Monday-Friday 9 am- 6 pm<br>
      Saturday 9 am- 1 pm<br>
      Sunday Closed
    </div>
  </section>

</div>
</body>
</html>
```